Inviting A6 Flyer for Church membership

We need an A6 size flyer for the church. We are looking for something fresh, inviting and impactful. Church new logo and current flyer design attached.
Back text as follows:
We would love to have you join us as our SPECIAL GUEST this Sunday at 10am.
You can find us at Harvest Lantern Family Church, 17-19 Marlow Crest Road
(Behind Brivo), Thornbury Meadow Village,QX4 7LB
For more information or for a chat, please call us on 07700 900418 / 07700 900752 or email church@hlfcuk-mail.test
Target Market(s)
Church
Industry/Entity Type
Church
Colors
Designer to choose colors to be used in the design.
Requirements
Must have
- fresh, inviting and impactful.
- Chruch logo (attached)
Should not have
- Too much going on

```html
<!DOCTYPE html>
<html lang="en">
<head>
<meta charset="utf-8">
<title>Harvest Lantern Family Church – Special Guest Flyer</title>
<link href="https://fonts.googleapis.com/css2?family=Cinzel:wght@400;700&family=Great+Vibes&family=Josefin+Slab:wght@400;700&display=swap" rel="stylesheet">
<style>
  :root {
    --bg: #7a7a7a;
    --brand-red: #a8342a;
    --photo-red: #b5473c;
    --photo-dark: #5e2520;
    --photo-sky: #a9d3e6;
    --white: #ffffff;
  }
  * { margin: 0; padding: 0; box-sizing: border-box; }
  html, body { width: 880px; height: 1200px; overflow: hidden; }
  body { background: var(--bg); position: relative; }

  .card { position: absolute; left: 98px; width: 684px; height: 486px; overflow: hidden; }
  .card--front { top: 78px; }
  .card--back { top: 636px; }

  .photo-area { position: absolute; inset: 0; }
  .card--front .photo-area {
    background: radial-gradient(circle at 50% 62%, var(--photo-red) 0%, #a03a30 45%, var(--photo-dark) 100%);
  }
  .card--back .photo-area {
    background: radial-gradient(circle at 50% 50%, #c86a5c 0%, #d89a8c 55%, var(--photo-sky) 100%);
  }

  /* Front */
  .logo-band {
    position: absolute; left: 0; top: 0; width: 100%; height: 242px;
    background: linear-gradient(to bottom, rgba(255,255,255,0.15) 0%, rgba(255,255,255,0.85) 55%, #fff 80%);
  }
  .frame-top {
    position: absolute; left: 14px; top: 14px; width: 656px; height: 228px;
    border: 5px solid var(--brand-red); border-bottom: none;
  }
  .frame-bottom {
    position: absolute; left: 14px; top: 242px; width: 656px; height: 216px;
    border: 4px solid var(--white); border-top: none;
  }
  .church-name {
    position: absolute; left: 0; top: 72px; width: 100%; text-align: center;
  }
  .church-name__dot {
    width: 56px; height: 56px; border-radius: 50%; background: var(--brand-red);
    margin: 0 auto 16px;
  }
  .church-name__text {
    font-family: "Cinzel", serif; font-weight: 400; color: var(--brand-red);
    font-size: 26px; line-height: 30px; letter-spacing: 0.5px;
  }
  .headline {
    position: absolute; left: 0; top: 268px; width: 100%; text-align: center; color: var(--white);
  }
  .headline-script { font-family: "Great Vibes", cursive; font-size: 92px; line-height: 90px; }
  .headline-caps {
    font-family: "Cinzel", serif; font-weight: 700; font-size: 62px; line-height: 72px; letter-spacing: 2px;
  }

  /* Back */
  .back-panel {
    position: absolute; left: 22px; top: 22px; width: 640px; height: 442px;
    background: rgba(142, 42, 34, 0.9);
  }
  .back-frame {
    position: absolute; left: 14px; top: 14px; width: 656px; height: 458px;
    border: 5px solid var(--white);
  }
  .invite-text {
    position: absolute; left: 22px; top: 94px; width: 640px; text-align: center;
    font-family: "Josefin Slab", serif; font-size: 26px; line-height: 31px; color: var(--white);
  }
  .invite-text p + p { margin-top: 31px; }
  .invite-text strong { font-weight: 700; }
</style>
</head>
<body>

<section class="card card--front">
  <div class="photo-area" role="img" aria-label="Photo of many hands reaching together toward the centre, tinted red"></div>
  <div class="logo-band"></div>
  <div class="frame-top"></div>
  <div class="frame-bottom"></div>
  <div class="church-name">
    <div class="church-name__dot"></div>
    <div class="church-name__text">Harvest Lantern<br>Ministries</div>
  </div>
  <div class="headline">
    <div class="headline-script">Be Our</div>
    <div class="headline-caps">Special Guest</div>
  </div>
</section>

<section class="card card--back">
  <div class="photo-area" role="img" aria-label="Photo of many hands reaching together against a pale sky"></div>
  <div class="back-panel"></div>
  <div class="back-frame"></div>
  <div class="invite-text">
    <p>We would love to have you join us as our<br><strong>SPECIAL GUEST</strong> this Sunday at 10am.</p>
    <p>You can find us at Harvest Lantern Family<br>Church, 17-19 Marlow Crest Road<br>(Behind Brivo), Thornbury Meadow Village,QX4 7LB</p>
    <p>For more information or for a chat, please<br>call us on 07700 900418 / 07700 900752<br>or email <strong>church@hlfcuk-mail.test</strong></p>
  </div>
</section>

</body>
</html>
```